We need a complete design for our construction company KELSO CONSTRUCTION based in Auckland New Zealand, we need a logo, website, business card, vehicle design etc..
We are a mid to high-end construction company who work mostly on residential projects and some commercial.

What we want to see in the design;
Professional,
Architectural,
Simple,
Alternative,

We want the design to communicate professionalism, high quality wormanship and and quality service.

Target Market(s)

People looking for a quality building/ construction company

Industry/Entity Type

Construction Company

Contact Information for Business Card

KELSO CONSTRUCTION.co.nz
Remi Tulvane
remi@kelsoconstruction-example.co.nz
021 5870 463

Logo Text

KELSO CONSTRUCTION

Number of Pages Required

5+ page

Font styles to use
Sans Serif

Colors

Designer to choose colors to be used in the design.

Requirements
Must have
• Must appear high end, professional, quality, be simple, easy to use, give security to potential clients
Nice to have
• high-quality photos of our recent projects
• about us page
• blog page
• contact us page
• high quality content
Should not have
• should not be hard to use and have too much going on.

```html
<!DOCTYPE html>
<html lang="en">
<head>
<meta charset="utf-8">
<title>Kelso Construction</title>
<link href="https://fonts.googleapis.com/css2?family=Montserrat:wght@400;600;700;800&family=Open+Sans:wght@400;600;700&display=swap" rel="stylesheet">
<style>
:root{
  --orange:#ff5a1f;
  --orange-dark:#e2460f;
  --ink:#2b2b2b;
  --text:#444;
  --muted:#888;
  --light:#f4f4f4;
  --dark:#2a2a2a;
  --footer:#1f1f1f;
  --white:#fff;
}
*{margin:0;padding:0;box-sizing:border-box}
html,body{width:1200px;height:3863px;overflow:hidden}
body{font-family:'Open Sans',sans-serif;color:var(--text);background:var(--white);position:relative}
.abs{position:absolute}
h1,h2,h3,.heading{font-family:'Montserrat',sans-serif}

/* top bar */
.topbar{position:absolute;top:0;left:0;width:1200px;height:62px;font-size:12px;color:#666;letter-spacing:.5px;border-bottom:1px solid #eee}
.topbar .hours{left:85px;top:24px}
.topbar .contact{right:85px;top:22px;display:flex;gap:26px;align-items:center}
.topbar .contact span{display:flex;align-items:center;gap:7px}

/* header */
.header{position:absolute;top:62px;left:0;width:1200px;height:100px}
.logo{left:85px;top:22px;display:flex;align-items:center;gap:12px}
.logo .mark{width:50px;height:50px;background:var(--orange)}
.logo .name{font-family:'Montserrat',sans-serif;font-weight:700;font-size:17px;line-height:21px;color:var(--ink)}
.nav{left:366px;top:44px;display:flex;gap:30px;font-family:'Montserrat',sans-serif;font-weight:600;font-size:12px;letter-spacing:1px;color:var(--ink);white-space:nowrap}
.nav .active{color:var(--orange);position:relative}
.nav .active:before{content:"";position:absolute;left:0;right:0;top:-44px;height:3px;background:var(--orange)}
.btn{display:inline-block;background:var(--orange);color:var(--white);font-family:'Montserrat',sans-serif;font-weight:700;font-size:12px;letter-spacing:1.5px;text-align:center;white-space:nowrap}
.header .btn{left:923px;top:36px;width:191px;height:30px;line-height:30px}

/* hero */
.hero{top:162px;left:0;width:1200px;height:530px;background:linear-gradient(100deg,#3b4048 0%,#55606b 45%,#6c6658 70%,#4a4a48 100%)}
.hero h1{left:85px;top:200px;font-size:37px;font-weight:800;color:var(--white);line-height:46px;letter-spacing:1px}
.hero h1 em{font-style:normal;color:var(--orange)}
.hero p{left:85px;top:310px;width:500px;font-family:'Montserrat',sans-serif;font-weight:600;font-size:13px;line-height:24px;color:var(--white);letter-spacing:.5px}
.hero .arrow{top:254px}

/* intro */
.helmet{left:528px;top:660px;width:144px;height:110px;background:radial-gradient(ellipse at 50% 45%,#fafafa 0%,#dcdcdc 60%,rgba(255,255,255,0) 72%)}
.intro-title{top:818px;left:0;width:1200px;text-align:center;font-family:'Montserrat',sans-serif;font-size:32px;font-weight:400;color:var(--ink);letter-spacing:2px}
.intro-sub{top:858px;left:0;width:1200px;text-align:center;font-family:'Montserrat',sans-serif;font-size:22px;font-weight:700;color:var(--orange);letter-spacing:1px}
.intro-text{top:912px;left:270px;width:660px;text-align:center;font-size:13px;line-height:22px;color:var(--text)}

.features{top:1004px;left:147px;width:906px;height:176px;display:flex}
.feature{flex:1;background:var(--orange);padding:20px 22px;color:var(--white);border-right:1px solid rgba(255,255,255,.3)}
.feature:nth-child(2){background:#ff4a10}
.feature:last-child{border:none;background:#ff6a2e}
.feature h3{font-size:16px;font-weight:700;letter-spacing:2px;display:flex;align-items:center;gap:8px;margin-bottom:14px}
.feature p{font-size:11.5px;line-height:17px;opacity:.9}
.feature a{display:inline-block;margin-top:14px;font-size:10px;font-weight:700;letter-spacing:1px;color:var(--white);text-decoration:underline}

/* services */
.services{top:1233px;left:0;width:1200px;height:356px;background:linear-gradient(160deg,#4a4846 0%,#6a4f40 45%,#8f3b22 70%,#a8401e 100%)}
.services h2{top:50px;left:0;width:1200px;text-align:center;font-size:34px;font-weight:700;color:var(--white);letter-spacing:1.5px}
.service{top:122px;width:220px;text-align:center;color:var(--white)}
.service .ring{width:112px;height:112px;margin:0 auto;border:4px solid var(--white);border-radius:50%;display:flex;align-items:center;justify-content:center}
.service.hot .ring{background:var(--orange)}
.service h3{margin-top:22px;font-size:15px;font-weight:600;letter-spacing:2px;line-height:21px}

/* projects split */
.photo{position:absolute}
.split-text .eyebrow{font-family:'Montserrat',sans-serif;font-weight:700;font-size:12px;color:var(--ink);letter-spacing:1px}
.split-text h2{font-size:36px;font-weight:800;color:#444;line-height:36px;margin:12px 0 24px;letter-spacing:1px}
.split-text p{font-size:13px;line-height:20px;color:var(--text);margin-bottom:20px}
.split-text .btn{width:190px;height:30px;line-height:30px;margin-top:4px}
.notch{position:absolute;width:0;height:0;border-top:14px solid transparent;border-bottom:14px solid transparent}

/* gallery */
.gallery{top:2516px;left:0;width:1200px;height:631px;background:linear-gradient(180deg,#2b2b2b,#1f1f1f)}
.gallery h2{top:48px;left:0;width:1200px;text-align:center;font-size:34px;font-weight:700;color:var(--white);letter-spacing:1.5px}
.tile{position:absolute;width:324px}
.tile.featured{background:var(--orange);display:flex;align-items:center;justify-content:center}

/* blog */
.blog h2{top:3192px;left:0;width:1200px;text-align:center;font-size:34px;font-weight:700;color:#444;letter-spacing:1.5px}
.post{top:3268px;width:324px}
.post .img{height:141px;position:relative}
.post .date{position:absolute;left:10px;top:0;background:var(--orange);color:var(--white);font-size:10px;font-weight:700;padding:4px 14px}
.post h3{font-family:'Open Sans',sans-serif;font-size:16px;font-weight:400;color:#333;line-height:26px;margin-top:22px;padding-right:30px}
.post .meta{margin-top:18px;font-size:11px;font-weight:700;color:#333}
.blog .btn{left:504px;top:3553px;width:192px;height:28px;line-height:28px}

/* footer */
.footer{top:3636px;left:0;width:1200px;height:227px;background:var(--footer);color:#ccc;font-size:12px}
.footer .logo{left:85px;top:36px}
.footer .logo .name{color:var(--white)}
.footer .copy{left:85px;top:122px;line-height:20px}
.fcol{top:52px}
.fcol h4{font-family:'Montserrat',sans-serif;font-size:11px;font-weight:600;letter-spacing:2px;color:var(--white);margin-bottom:16px}
.fcol li{list-style:none;line-height:20px}
.fcol .row{display:flex;gap:8px;line-height:16px;margin-bottom:12px}
.footer .btn{left:922px;top:58px;width:190px;height:28px;line-height:28px}
.socials{left:930px;top:110px;display:grid;grid-template-columns:repeat(4,14px);gap:30px 38px}
.socials span{width:12px;height:12px;border-radius:50%;background:var(--white)}
.to-top{left:1122px;top:3600px;width:40px;height:40px;background:var(--orange);display:flex;align-items:center;justify-content:center}
</style>
</head>
<body>

<div class="topbar">
  <div class="abs hours">MON – SAT: 7.00 – 18.00 &nbsp; SUNDAY: CLOSED &nbsp; EMERGENCY: 24HR / 7DAYS</div>
  <div class="abs contact">
    <span><svg width="9" height="14" viewBox="0 0 9 14"><rect x="0.5" y="0.5" width="8" height="13" rx="1.5" fill="none" stroke="#ff5a1f"/><circle cx="4.5" cy="11" r="1" fill="#ff5a1f"/></svg>+(09) 555 0148</span>
    <span><svg width="14" height="10" viewBox="0 0 14 10"><rect width="14" height="10" fill="#ff5a1f"/><path d="M0 0l7 6 7-6" fill="none" stroke="#fff"/></svg>hello@kelsobuild-example.co.nz</span>
  </div>
</div>

<header class="header">
  <div class="abs logo"><div class="mark"></div><div class="name">KELSO<br>CONSTRUCTION</div></div>
  <nav class="abs nav"><span class="active">HOME</span><span>ABOUT</span><span>PROJECTS</span><span>SERVICES</span><span>NEWS</span><span>CONTACT</span></nav>
  <a class="abs btn">GET A FREE QUOTE</a>
</header>

<section class="abs hero" role="img" aria-label="Engineers in hard hats and safety vests reviewing plans on a construction site">
  <h1 class="abs">PERFECTION IS <em>ALWAYS UNDER</em><br>CONSTUCTION</h1>
  <p class="abs">LOREM IPSUM IS SIMPLY DUMMY TEXT OF THE PRINTING AND STANDARD DUMMY TEXT EVER.</p>
  <svg class="abs arrow" style="left:22px" width="24" height="20" viewBox="0 0 24 20"><path d="M22 10H3M10 3L3 10l7 7" fill="none" stroke="#fff" stroke-width="2"/></svg>
  <svg class="abs arrow" style="left:1152px" width="24" height="20" viewBox="0 0 24 20"><path d="M2 10h19M14 3l7 7-7 7" fill="none" stroke="#fff" stroke-width="2"/></svg>
</section>

<div class="abs helmet" role="img" aria-label="White safety helmet"></div>
<h2 class="abs intro-title">WE ARE INTRO...</h2>
<div class="abs intro-sub">TELL THE WORLD ABOUT YOURSELF</div>
<p class="abs intro-text">Ut wisi enim ad minim veniam, quis nostrud exerci tation ullamcorperadipiscing elit, sed diam nonummy nibh suscipit lobortis nisl ut aliquip ex ea commodo consequat.</p>

<div class="abs features">
  <div class="feature">
    <h3><svg width="14" height="16" viewBox="0 0 14 16"><path d="M7 1a5 5 0 0 0-5 5c0 4 5 9 5 9s5-5 5-9a5 5 0 0 0-5-5z" fill="#fff"/><circle cx="7" cy="6" r="2" fill="#ff5a1f"/></svg>MOTIVATION</h3>
    <p>Mauris accumsan eros eget libero posuere vulputate. Etiam elit elit, elementum sed varius at, adipiscing vitae est. Sed nec felis pellentesque, lacinia dui sed.</p>
    <a>LOREM US</a>
  </div>
  <div class="feature">
    <h3><svg width="14" height="14" viewBox="0 0 14 14"><rect x="1" y="1" width="12" height="12" fill="none" stroke="#fff" stroke-width="1.5"/><path d="M4 5h6M4 8h6M4 11h4" stroke="#fff"/></svg>HISTORY</h3>
    <p>Mauris accumsan eros eget libero posuere vulputate. Etiam elit elit, elementum sed varius at, adipiscing vitae est. Sed nec felis pellentesque.</p>
    <a>MORE</a>
  </div>
  <div class="feature">
    <h3><svg width="14" height="16" viewBox="0 0 14 16"><circle cx="7" cy="6" r="5" fill="none" stroke="#fff" stroke-width="1.5"/><path d="M4 10l-1 5 4-2 4 2-1-5" fill="none" stroke="#fff" stroke-width="1.5"/></svg>CERTIFICATES</h3>
    <p>Mauris accumsan eros eget libero posuere vulputate. Etiam elit elit, elementum sed varius at, adipiscing vitae est. Sed nec felis pulton.</p>
    <a>MORE</a>
  </div>
</div>

<section class="abs services" aria-label="Our services">
  <h2 class="abs">OUR SERVICES</h2>
  <div class="abs service" style="left:121px"><div class="ring"><svg width="48" height="48" viewBox="0 0 48 48" fill="none" stroke="#fff" stroke-width="2"><rect x="8" y="10" width="32" height="28"/><path d="M14 32V18l8-4 8 4v14M8 38h32"/></svg></div><h3>ARCHITECTURAL<br>DESIGN</h3></div>
  <div class="abs service" style="left:376px"><div class="ring"><svg width="48" height="48" viewBox="0 0 48 48" fill="none" stroke="#fff" stroke-width="2"><circle cx="24" cy="24" r="14"/><circle cx="24" cy="24" r="5"/><path d="M24 6v6M24 36v6M6 24h6M36 24h6"/></svg></div><h3>RECONSTRUCTION<br>SERVICES</h3></div>
  <div class="abs service" style="left:616px"><div class="ring"><svg width="48" height="48" viewBox="0 0 48 48" fill="none" stroke="#fff" stroke-width="2"><rect x="16" y="8" width="16" height="14"/><path d="M24 22v6M21 28h6v14h-6z"/></svg></div><h3>REFURBISHMENT</h3></div>
  <div class="abs service hot" style="left:854px"><div class="ring"><svg width="48" height="48" viewBox="0 0 48 48" fill="none" stroke="#fff" stroke-width="2"><path d="M8 22L24 10l16 12M12 20v18h24V20"/><rect x="20" y="26" width="8" height="12"/></svg></div><h3>HOUSE<br>EXTENSIONS</h3></div>
</section>

<div class="photo" style="left:147px;top:1643px;width:453px;height:409px;background:linear-gradient(160deg,#3f86d4 0%,#8ec1ee 45%,#6f7b88 70%,#c7c4bb 100%)" role="img" aria-label="Residential house roof against a blue sky"></div>
<div class="notch" style="left:586px;top:1833px;border-right:14px solid #fff"></div>
<div class="abs split-text" style="left:649px;top:1690px;width:340px">
  <div class="eyebrow">LOREM IPSUM</div>
  <h2>RESIDENTIAL<br>PROJECTS</h2>
  <p>Ut wisi enim ad minim veniam, quis nostrud exerci tation ullamcorperadipiscing elit, sed diam nonummy nibh suscipit lobortis nisl ut aliquip ex ea commodo consequat.</p>
  <p>Ut wisi enim ad minim veniam, quis nostrud exerci tation ullamcorperadipiscing elit, sed diam nonummy</p>
  <a class="btn">READ MORE</a>
</div>

<div class="abs split-text" style="left:200px;top:2094px;width:327px;text-align:right">
  <div class="eyebrow">LOREM IPSUM</div>
  <h2>COMMERCIAL<br>PROJECTS</h2>
  <p>Ut wisi enim ad minim veniam, quis nostrud exerci tation ullamcorperadipiscing elit, sed diam nonummy nibh suscipit lobortis nisl ut aliquip ex ea commodo consequat.</p>
  <p>Ut wisi enim ad minim veniam, quis nostrud exerci tation ullamcorperadipiscing elit, sed diam nonummy</p>
  <a class="btn">READ MORE</a>
</div>
<div class="photo" style="left:600px;top:2052px;width:453px;height:410px;background:linear-gradient(180deg,#cfd6de 0%,#7e8c9a 40%,#3b4652 100%)" role="img" aria-label="Glass office towers seen from below"></div>
<div class="notch" style="left:600px;top:2243px;border-left:14px solid #fff"></div>

<section class="abs gallery" aria-label="Our projects">
  <h2 class="abs">OUR PROJECTS</h2>
  <div class="tile featured" style="left:85px;top:136px;height:207px"><svg width="74" height="80" viewBox="0 0 74 80" fill="none" stroke="#fff" stroke-width="3"><circle cx="37" cy="37" r="34"/><path d="M37 16v42M16 37h42"/></svg></div>
  <div class="tile" style="left:438px;top:136px;height:207px;background:linear-gradient(135deg,#6b5a4a,#2e2a26)" role="img" aria-label="Engineers in safety vests on site"></div>
  <div class="tile" style="left:788px;top:136px;height:207px;background:linear-gradient(135deg,#c9a46a,#7b5b2e 60%,#d8c49a)" role="img" aria-label="Timber roof framing"></div>
  <div class="tile" style="left:85px;top:368px;height:211px;background:linear-gradient(135deg,#a8794a,#5a3b20)" role="img" aria-label="Timber wall frame under construction"></div>
  <div class="tile" style="left:438px;top:368px;height:211px;background:linear-gradient(180deg,#7fb0e0,#a58e70 50%,#5a4a3a)" role="img" aria-label="Building facades with a tower crane"></div>
  <div class="tile" style="left:788px;top:368px;height:211px;background:linear-gradient(135deg,#6a6a66,#2a2a28)" role="img" aria-label="Workers on scaffolding"></div>
</section>

<section class="blog" aria-label="Our blog">
  <h2 class="abs">OUR BLOG</h2>
  <div class="abs post" style="left:85px"><div class="img" style="background:linear-gradient(135deg,#9cc0e2,#3e6f9e)" role="img" aria-label="Modern glass building"><span class="date">14 SEP</span></div><h3>Provide Quality Productivity With Certified Engineers</h3><div class="meta">AUGUST 1, 2017 / Comment 0 / admin</div></div>
  <div class="abs post" style="left:438px"><div class="img" style="background:linear-gradient(135deg,#c98c72,#8a4a38)" role="img" aria-label="Clay roof tiles"><span class="date">14 SEP</span></div><h3>Provide Quality Productivity With Certified Engineers</h3><div class="meta">AUGUST 1, 2017 / Comment 0 / admin</div></div>
  <div class="abs post" style="left:788px"><div class="img" style="background:linear-gradient(135deg,#a8c8e6,#d8a24a 60%,#4a5a70)" role="img" aria-label="Team of builders in hard hats"><span class="date">8 SEP</span></div><h3>Provide Quality Productivity With Certified Engineers</h3><div class="meta">AUGUST 1, 2017 / Comment 0 / admin</div></div>
  <a class="abs btn">VIEW ALL</a>
</section>

<div class="abs to-top"><svg width="18" height="12" viewBox="0 0 18 12"><path d="M2 10l7-7 7 7" fill="none" stroke="#fff" stroke-width="2.5"/></svg></div>

<footer class="abs footer">
  <div class="abs logo"><div class="mark"></div><div class="name">KELSO<br>CONSTRUCTION</div></div>
  <div class="abs copy">© 2018 KELSO CONSTRUCTION<br>All Rights Reserved.</div>
  <div class="abs fcol" style="left:349px"><h4>SITEMAP</h4><ul><li>Home</li><li>About us</li><li>Blog</li><li>Contact us</li></ul></div>
  <div class="abs fcol" style="left:498px"><h4>ADDRESS</h4><ul><li>48 Harbour Lane,</li><li>Ponsonby, Auckland</li><li>New Zealand.</li></ul></div>
  <div class="abs fcol" style="left:677px"><h4>CALL US NOW!</h4>
    <div class="row"><svg width="9" height="14" viewBox="0 0 9 14"><rect x="0.5" y="0.5" width="8" height="13" rx="1.5" fill="none" stroke="#ccc"/></svg><div>CALL US TODAY<br>+64 (0) 9 555 0172</div></div>
    <div class="row"><svg width="12" height="9" viewBox="0 0 12 9"><rect width="12" height="9" fill="#ccc"/><path d="M0 0l6 5 6-5" fill="none" stroke="#1f1f1f"/></svg><div>SEND US A MESSAGE<br>office@kelsobuild-example.co.nz</div></div>
  </div>
  <a class="abs btn">GET A FREE QUOTE</a>
  <div class="abs socials"><span></span><span></span><span></span><span></span><span></span><span></span><span></span><span></span></div>
</footer>

</body>
</html>
```